Velvet Lagoon Charm Boutique

Looking to refresh our old business cards. We are a girls/tween birthday party store and salon specializing in princess, glamour and spa parties. I would like to maintain the same colors (hot pink and turquoise). Would like the card to be feminine, fun and glitzy..

Target Market(s)

Parents of girls and girls aged 4-14

Industry/Entity Type

Store

Font styles to use
Script

Colors
e34197
85cae6

Requirements
Must have
• name phone and address
colors of hot pink and turquoise
appointment day and time field on one side
Nice to have
• creativity
Should not have
• picture of lipstick

```html
<!DOCTYPE html>
<html lang="en">
<head>
<meta charset="utf-8">
<title>Velvet Lagoon Charm Boutique – Business Card</title>
<link rel="stylesheet" href="https://fonts.googleapis.com/css2?family=Josefin+Sans:wght@300;400&display=swap">
<style>
  :root {
    --card-cream: #fcebdc;
    --hot-pink: #e34197;
    --soft-pink: #f9cdee;
    --turquoise: #85cae6;
    --banner-aqua: #b3f7f6;
    --ink: #2a2a2a;
    --caption-ink: #555a5c;
    --field-white: #fffaf6;
    --page: #ffffff;
  }
  * { margin: 0; padding: 0; box-sizing: border-box; }
  html, body { width: 1200px; height: 1000px; overflow: hidden; background: var(--page); }
  body { position: relative; font-family: "Josefin Sans", sans-serif; color: var(--ink); }

  .card {
    position: absolute; left: 104px; width: 220px; height: 385px;
    background: var(--card-cream); overflow: hidden;
  }
  .card--front { top: 39px; }
  .card--back { top: 466px; }

  .balloon-cluster {
    position: absolute; left: 40px; top: 0; width: 140px; height: 100px;
    background: radial-gradient(ellipse 50% 55% at 50% 40%, #f7a6d6 0%, #f9cbe6 40%, #c3f2f4 70%, rgba(252,235,220,0) 100%);
  }
  .name-badge {
    position: absolute; left: 19px; top: 102px; width: 182px; height: 182px;
    border-radius: 50%; background: #fff; border: 4px solid var(--soft-pink);
    display: flex; align-items: center; justify-content: center; text-align: center;
  }
  .name-badge__name { font-size: 22px; line-height: 1.2; font-weight: 400; color: var(--hot-pink); }

  .contact { position: absolute; left: 0; right: 0; top: 300px; text-align: center; }
  .contact__name {
    font-size: 10.5px; line-height: 16px; color: var(--hot-pink); font-weight: 300; white-space: nowrap;
  }
  .contact__line { font-size: 11px; line-height: 15px; font-weight: 300; }
  .contact__phone { font-size: 11px; line-height: 15px; font-weight: 300; margin-top: 4px; }

  .appointment { position: absolute; left: 0; right: 0; top: 45px; }
  .appointment__label { font-size: 7.5px; letter-spacing: 0.6px; text-align: center; }
  .appointment__field {
    margin: 4px 0 0 33px; width: 180px; height: 16px; border-radius: 8px;
    background: var(--field-white); padding: 4px 0 0 8px;
    font-size: 7.5px; letter-spacing: 0.6px;
  }
  .faint-badge {
    position: absolute; left: 20px; top: 100px; width: 180px; height: 180px;
    border-radius: 50%; background: #fdf1ea;
    display: flex; align-items: center; justify-content: center; text-align: center;
  }
  .faint-badge__name { font-size: 22px; line-height: 1.2; color: #f3c4dc; }
  .balloon-field {
    position: absolute; left: 0; right: 0; bottom: 0; height: 170px;
    background: linear-gradient(180deg, rgba(252,235,220,0) 0%, #fbdfe3 35%, #dcf3ea 70%, var(--card-cream) 100%);
  }

  .caption-banner {
    position: absolute; left: 18px; top: 915px; width: 1163px; height: 66px;
    border-radius: 20px; background: var(--banner-aqua);
    display: flex; align-items: center; justify-content: center;
    font-size: 20px; font-weight: 300; letter-spacing: 3.5px; color: var(--caption-ink);
    white-space: nowrap;
  }
</style>
</head>
<body>
  <section class="card card--front">
    <div class="balloon-cluster" role="img" aria-label="Illustrated bunch of pastel pink and turquoise balloons"></div>
    <div class="name-badge">
      <p class="name-badge__name">Velvet Lagoon<br>Charm Boutique</p>
    </div>
    <div class="contact">
      <p class="contact__name">VELVET LAGOON CHARM BOUTIQUE</p>
      <p class="contact__line">48 Willow Bend Lane</p>
      <p class="contact__line">Harbor Glen, New York 10000</p>
      <p class="contact__phone">Phone : (555)014-2290</p>
    </div>
  </section>

  <section class="card card--back">
    <div class="appointment">
      <p class="appointment__label">YOUR APPOINTMENT WOULD BE ON</p>
      <p class="appointment__field">DAY :</p>
      <p class="appointment__field">DATE :</p>
    </div>
    <div class="faint-badge">
      <p class="faint-badge__name">Velvet Lagoon<br>Charm Boutique</p>
    </div>
    <div class="balloon-field" role="img" aria-label="Faint illustrated pastel balloons rising from the bottom edge"></div>
  </section>

  <div class="caption-banner">VELVET LAGOON CHARM BOUTIQUE (Business Card)</div>
</body>
</html>
```